Wordpress website design for a high-end painting business

We are currently rebranding and are looking to update our Wordpress theme. We have recently rebranded our logo on PixelHarbor, and would like our website to be equally as refined.
Our business is named “Kestrel Painters”. We are a high-end painting business that is known for being professional and having high standards. Our clean and professional image is important as it separates us from our competition. Our current website can be found at www.wrenfieldcoatings.co.nz . We designed the site ourselves so it is understandably rudimentary. We are generally happy with the. page layout of our existing site, but we like a professional remodel. Any ideas on improvement welcomed.
We would like the front page of the website to summarise all of the info throughout the whole website (I.e introduction, photos, testimonials, contact info etc.) as visitors typically scroll through the first page to see that we are reputable and get to our contact number/email contact at the bottom of the page. We would like this first page to give a clean well rounded image of our business. We would like the gallery to be a scroll through of large photos, as it is difficult to see paint details in smaller photos. A contact page with an enquiry section would also be good.
For the colour scheme, we would like something that fits a bold, masculine and high end theme (similar to our logo attached).
We would like the footer to include Veltora paint logos and the accredited painter logo we have included as these are important to our profession.
We have attached some photos of our work also. I will add more in the coming days. More can also be found on our website.
If you have questions or comments, please don’t hesitate to ask and I will get back as soon as possible.
We are open to your own interpretation or ideas for a better layout/site provided they fit the general brief of being a well rounded site for our profession.
Thanks,
Kestrel Painters.
Target Market(s)
High end clients
Industry/Entity Type
Painting (interior and exterior)
Coding
Coded - Design and coding required
Requirements
Must have
- Classy feel, separating us from typical painting companies. Well rounded homepage.
Nice to have
- Lots of examples of our work
Should not have
- Untidy paint motifs (eg, paint droplets, paint splashes)

```html
<!DOCTYPE html>
<html lang="en">
<head>
<meta charset="utf-8">
<title>Kestrel Painters</title>
<link href="https://fonts.googleapis.com/css2?family=Noticia+Text:wght@400;700&family=Noto+Serif:wght@400;700&family=Lato:wght@400;700&display=swap" rel="stylesheet">
<style>
:root{
  --navy:#1c2333;
  --brown:#6b5233;
  --brown-soft:#8a6d4a;
  --ink:#1a1a1a;
  --muted:#5a5a5a;
  --paper:#ffffff;
  --panel:#f4f5f7;
  --footer:#0b0d12;
  --star:#f2b01e;
}
*{box-sizing:border-box;margin:0;padding:0}
html,body{width:1200px;height:4231px;overflow:hidden}
body{position:relative;background:var(--paper);font-family:"Noto Serif",serif;color:var(--ink)}
.abs{position:absolute}
h1,h2,h3{font-family:"Noticia Text",serif;font-weight:700}
.btn{position:absolute;display:flex;align-items:center;justify-content:center;border-radius:32px;font-family:"Noticia Text",serif;font-weight:700;font-size:21px}
.btn-brown{background:var(--brown);color:#fff}
.btn-white{background:#fff;color:var(--brown)}

/* top bar */
.topbar{left:0;top:0;width:1200px;height:64px;background:var(--navy)}
.topbar .social{position:absolute;top:20px;width:22px;height:22px;border:1.5px solid #fff;border-radius:50%}
.topbar .info{position:absolute;top:20px;color:#fff;font-size:15px;display:flex;align-items:center;gap:8px}
.topbar .info svg{width:22px;height:22px}

/* nav */
.nav{left:0;top:64px;width:1200px;height:79px;background:#fff}
.nav a{position:absolute;top:27px;font-family:"Noticia Text",serif;font-weight:700;font-size:17px;color:var(--ink);text-decoration:none}
.nav .contact-pill{top:18px;left:952px;width:94px;height:40px;border-radius:20px;background:var(--brown);color:#fff;display:flex;align-items:center;justify-content:center}
.brand{left:108px;top:72px;width:144px;height:144px;border-radius:50%;background:#fff;box-shadow:0 2px 6px rgba(0,0,0,.15);display:flex;flex-direction:column;align-items:center;justify-content:center;z-index:5}
.brand .dot{width:34px;height:34px;border-radius:50%;background:var(--navy);margin-bottom:8px}
.brand span{font-family:"Noticia Text",serif;font-weight:700;font-size:15px;color:var(--navy);line-height:1.15;text-align:center}

/* hero */
.hero{left:0;top:143px;width:1200px;height:628px;background:linear-gradient(180deg,#6f8fb0 0%,#a9b7a0 30%,#b79c7d 48%,#5f7a38 72%,#46652a 100%)}
.hero h1{position:absolute;left:108px;top:175px;font-size:56px;line-height:53px;color:#fff}
.hero p{position:absolute;left:112px;top:290px;font-size:20px;line-height:27px;color:#fff}

/* about */
.about-photo{left:112px;top:858px;width:407px;height:407px;border-radius:50%;background:linear-gradient(160deg,#c9ccd1 0%,#e9e6dc 40%,#7d8a5f 85%)}
.about-ring{left:130px;top:876px;width:371px;height:371px;border-radius:50%;border:4px solid #fff}
.sec-title{display:flex;align-items:center;gap:24px;font-size:37px;color:var(--ink)}
.sec-title .rule{width:76px;height:2px;background:var(--ink)}
.about-text{left:582px;top:916px;width:500px;font-size:17px;line-height:26px;color:var(--ink)}
.about-text p+p{margin-top:26px}

/* services */
.services{left:0;top:1350px;width:1200px;height:840px;background:linear-gradient(180deg,var(--navy) 0%,#262d3d 45%,#2f3443 70%,var(--navy) 100%)}
.light-title{color:#fff;justify-content:center}
.light-title .rule{background:#fff}
.services .lead{position:absolute;left:0;width:1200px;top:194px;text-align:center;color:#fff;font-size:17px;line-height:26px}
.svc-photo{position:absolute;border-radius:50%}
.svc-feature{position:absolute;left:395px;top:288px;width:410px;height:410px;border-radius:50%;background:radial-gradient(circle,#7a6550 0%,#5e4a35 70%);border:10px solid var(--brown-soft)}
.svc-feature .ring{position:absolute;left:0;top:0;width:390px;height:390px;border-radius:50%;border:3px solid #fff}
.svc-feature h3{position:absolute;top:70px;width:100%;text-align:center;color:#fff;font-size:27px}
.svc-feature p{position:absolute;top:124px;left:28px;width:334px;text-align:center;color:#fff;font-size:14.5px;line-height:26px}
.arrow{position:absolute;width:44px;height:24px}

/* testimonials */
.quote{left:0;top:2370px;width:1200px;text-align:center;font-size:16.5px;line-height:26px;color:var(--muted)}
.rating{left:0;top:2510px;width:1200px;display:flex;justify-content:center;align-items:center;gap:6px;font-size:16px}
.rating b{font-weight:700}

/* gallery */
.gallery{left:0;top:2690px;width:1200px;height:556px;background:linear-gradient(180deg,#6c5638 0%,#7c6445 50%,#6a5436 100%)}
.gal-item{position:absolute;top:206px;width:222px;height:222px;border-radius:50%;border:6px solid #b7a88f}

/* contact */
.talk h2{font-size:37px}
.talk p{font-size:16px;line-height:31px;font-weight:700;margin-top:14px}
.talk h3{font-size:21px;margin-top:30px;white-space:nowrap}
.talk .icons{display:flex;gap:16px;margin-top:16px}
.talk .icons span{width:40px;height:40px;border-radius:6px;background:var(--navy)}
.contact-box{left:558px;top:3333px;width:529px;height:397px;background:var(--panel);border:1px solid #e3e4e8}
.contact-box h3{position:absolute;top:30px;width:100%;text-align:center;font-size:26px}
.field{position:absolute;height:48px;border:1px solid #9aa0a8;background:#fff;font-family:"Noticia Text",serif;font-weight:700;font-size:15px;color:#444;padding:14px 18px}

/* footer */
.footer{left:0;top:3775px;width:1200px;height:456px;background:var(--footer);color:#fff}
.footer h4{position:absolute;top:117px;font-family:"Noticia Text",serif;font-weight:700;font-size:21px}
.footer ul{position:absolute;top:160px;list-style:none;font-size:15px;line-height:31px}
.footer li::before{content:"";display:inline-block;width:7px;height:7px;border-radius:50%;background:#fff;margin-right:10px;vertical-align:middle}
.footer .blurb{position:absolute;left:112px;top:145px;width:300px;font-family:Lato,sans-serif;font-size:12px;line-height:21px;color:#c9c9c9}
.footer .sub{position:absolute;left:108px;top:264px;width:306px;height:40px;display:flex}
.footer .sub span{flex:1;background:#fff;color:#888;font-family:Lato,sans-serif;font-size:10px;padding:14px 20px}
.footer .sub b{width:120px;background:var(--brown);color:#fff;font-family:Lato,sans-serif;font-weight:400;font-size:15px;display:flex;align-items:center;justify-content:center}
.footer .addr{position:absolute;left:868px;top:160px;font-size:15px;line-height:34px}
.footer .addr div{display:flex;align-items:center;gap:14px}
.footer .addr i{width:20px;height:20px;border:1.5px solid #fff;border-radius:50%;display:inline-block}
.footer .copy{position:absolute;left:112px;top:405px;font-family:Lato,sans-serif;font-size:11px}
.badge{position:absolute;top:403px;height:16px}
</style>
</head>
<body>

<!-- top bar -->
<header class="abs topbar">
  <span class="social" style="left:113px" aria-label="Social profile"></span>
  <span class="social" style="left:152px" aria-label="Social profile"></span>
  <span class="social" style="left:191px" aria-label="Social profile"></span>
  <span class="social" style="left:230px" aria-label="Social profile"></span>
  <div class="info" style="left:533px">
    <svg viewBox="0 0 24 24" fill="none" stroke="#fff" stroke-width="1.5"><circle cx="12" cy="12" r="10"/><path d="M8.5 7.5l2 2-1 1.5c.8 1.5 2 2.7 3.5 3.5l1.5-1 2 2-1.2 1.3c-3.5-.5-7.2-4.2-7.7-7.7z" fill="#fff"/></svg>
    021 555 0148
  </div>
  <div class="info" style="left:682px">
    <svg viewBox="0 0 24 24" fill="none" stroke="#fff" stroke-width="1.5"><circle cx="12" cy="12" r="10"/><rect x="7" y="8.5" width="10" height="7" fill="#fff" stroke="none"/></svg>
    hello@kestrelpainters.co.nz
  </div>
  <div class="info" style="left:924px">
    <svg viewBox="0 0 24 24" fill="none" stroke="#fff" stroke-width="1.5"><circle cx="12" cy="12" r="10"/><path d="M12 6.5a3.5 3.5 0 0 1 3.5 3.5c0 2.5-3.5 7-3.5 7s-3.5-4.5-3.5-7A3.5 3.5 0 0 1 12 6.5z"/></svg>
    Fernleigh, Northvale
  </div>
</header>

<!-- navigation -->
<nav class="abs nav">
  <a style="left:338px">Home</a>
  <a style="left:446px">Services</a>
  <a style="left:573px">Gallery</a>
  <a style="left:693px">About</a>
  <a style="left:802px">Testimonials</a>
  <a class="contact-pill">Contact</a>
  <svg class="abs" style="left:1070px;top:30px" width="16" height="16" viewBox="0 0 16 16" fill="none" stroke="#1a1a1a" stroke-width="2"><circle cx="6.5" cy="6.5" r="5"/><path d="M10.5 10.5l4 4"/></svg>
</nav>
<div class="abs brand"><div class="dot"></div><span>KESTREL<br>PAINTERS</span></div>

<!-- hero -->
<section class="abs hero" role="img" aria-label="Photo of a large two-storey painted home with a green lawn and garden">
  <h1>Welcome to<br>Kestrel Painters</h1>
  <p>Here at Kestrel Painters, we take a lot of<br>pride in our work.</p>
  <div class="btn btn-white" style="left:112px;top:360px;width:172px;height:60px">Get Started</div>
</section>

<!-- about -->
<div class="abs about-photo" role="img" aria-label="Photo of a freshly painted single-storey house"></div>
<div class="abs about-ring"></div>
<h2 class="abs sec-title" style="left:582px;top:846px">About Us <span class="rule"></span></h2>
<div class="abs about-text">
  <p>Here at Kestrel Painters, we take a lot of pride in our work. We strive to ensure the highest quality paint-work, paying close attention to detail to provide a long lasting finish. Our clients are always our priority, we aim to deliver beyond their expectations.</p>
  <p>It is our goal to provide an excellent service from start to finish through clear communication, free quoting and transparency with our pricing.We take great pride in the preparation of surfaces for painting and only use the best quality products to ensure we achieve the best finish for you.</p>
</div>
<div class="btn btn-brown" style="left:582px;top:1225px;width:172px;height:62px">Read More</div>

<!-- services -->
<section class="abs services" role="img" aria-label="Dimmed photo of a painted house behind the services carousel">
  <h2 class="abs sec-title light-title" style="left:0;width:1200px;top:134px">
    <span class="rule"></span>Services<span class="rule"></span>
  </h2>
  <p class="lead">It is our goal to provide an excellent service from start to finish through clear<br>communication, free quoting and transparency with our pricing.</p>
  <div class="svc-photo" style="left:112px;top:356px;width:248px;height:274px;background:linear-gradient(170deg,#8fb0d6 0%,#dcdcd8 45%,#6e9a3c 80%)" role="img" aria-label="Photo of a painted two-storey home"></div>
  <div class="svc-photo" style="left:838px;top:356px;width:248px;height:274px;background:linear-gradient(160deg,#7e8a86 0%,#5d6b66 55%,#c8c3b8 100%)" role="img" aria-label="Photo of an interior wall with patterned wallpaper"></div>
  <div class="svc-feature" role="img" aria-label="Photo of a painted interior room">
    <div class="ring"></div>
    <h3>Interior Painting</h3>
    <p>we aim to deliver beyond their expectations. It is our goal to provide an excellent service from start to finish through clear communication, free quoting and transparency with our pricing.</p>
    <div class="btn btn-white" style="left:113px;top:262px;width:164px;height:58px">Learn More</div>
  </div>
  <svg class="arrow" style="left:20px;top:470px" viewBox="0 0 44 24" fill="none" stroke="#9aa0ac" stroke-width="2"><path d="M42 12H3M13 3L3 12l10 9"/></svg>
  <svg class="arrow" style="left:1126px;top:470px" viewBox="0 0 44 24" fill="none" stroke="#fff" stroke-width="2"><path d="M2 12h39M31 3l10 9-10 9"/></svg>
</section>

<!-- testimonials -->
<h2 class="abs sec-title" style="left:0;width:1200px;top:2244px;justify-content:center">
  <span class="rule"></span>Testimonials<span class="rule"></span>
</h2>
<svg class="abs" style="left:578px;top:2315px" width="42" height="30" viewBox="0 0 42 30" fill="#555"><path d="M0 14Q0 2 14 0v6Q8 7 8 12h8v18H0zM22 14Q22 2 36 0v6Q30 7 30 12h8v18H22z"/></svg>
<p class="abs quote">Just had our house interior painted throughout by Kestrel. They were professional right from the start. They<br>turned up to give a quote when other firms never responded. They were spot on with their time and cost<br>estimates and never missed a day ..we had to ask them not to work on Public Holidays. They have an attention<br>to detail and a level of care that is above what I’ve seen previously. If you’re lucky enough to be able to secure<br>their services then good for you – Affable, professional, young firm – I would use them again</p>
<div class="abs rating">
  <svg width="130" height="20" viewBox="0 0 130 20" fill="#f2b01e">
    <path id="star" d="M10 1l2.6 6 6.4.5-4.9 4.2 1.5 6.3L10 14.6 4.4 18l1.5-6.3L1 7.5l6.4-.5z"/>
    <use href="#star" x="26"/><use href="#star" x="52"/><use href="#star" x="78"/><use href="#star" x="104"/>
  </svg>
  <span>&nbsp;Thanks.&nbsp;&nbsp;<b>DANIEL MORROW (2020)</b></span>
</div>
<div class="btn btn-brown" style="left:513px;top:2563px;width:172px;height:62px">View All</div>

<!-- gallery -->
<section class="abs gallery" role="img" aria-label="Brown-toned photo of a painted house behind the gallery carousel">
  <h2 class="abs sec-title light-title" style="left:0;width:1200px;top:128px">
    <span class="rule"></span>Gallery<span class="rule"></span>
  </h2>
  <div class="gal-item" style="left:110px;background:linear-gradient(170deg,#9fb6d0 0%,#e2e2df 45%,#5f8a3a 85%)" role="img" aria-label="Photo of a painted two-storey home"></div>
  <div class="gal-item" style="left:364px;background:linear-gradient(170deg,#a9c0dc 0%,#8a8f98 50%,#6f7a86 100%)" role="img" aria-label="Photo of a house with painted weatherboards"></div>
  <div class="gal-item" style="left:613px;background:linear-gradient(160deg,#7e8a86 0%,#5d6b66 55%,#c8c3b8 100%)" role="img" aria-label="Photo of an interior wall with patterned wallpaper"></div>
  <div class="gal-item" style="left:865px;background:linear-gradient(170deg,#e6e2dc 0%,#bdb4a9 50%,#5e6068 100%)" role="img" aria-label="Photo of a painted living room with carpet"></div>
  <svg class="arrow" style="left:30px;top:305px" viewBox="0 0 44 24" fill="none" stroke="#fff" stroke-width="2"><path d="M42 12H3M13 3L3 12l10 9"/></svg>
  <svg class="arrow" style="left:1136px;top:305px" viewBox="0 0 44 24" fill="none" stroke="#fff" stroke-width="2"><path d="M2 12h39M31 3l10 9-10 9"/></svg>
</section>

<!-- contact -->
<div class="abs talk" style="left:112px;top:3400px;width:420px">
  <h2>Let’s Talk</h2>
  <p>If you are looking at painting your property, or<br>have any questions, please don’t hesitate to call<br>Ravi on 021 5550148.</p>
  <h3>Stay Tuned with is on Social Networks</h3>
  <div class="icons"><span aria-label="Social profile"></span><span aria-label="Social profile"></span><span aria-label="Social profile"></span><span aria-label="Social profile"></span></div>
</div>
<section class="abs contact-box">
  <h3>Contact us</h3>
  <div class="field" style="left:33px;top:95px;width:222px">First Name*</div>
  <div class="field" style="left:282px;top:95px;width:222px">Last Name*</div>
  <div class="field" style="left:33px;top:158px;width:222px">Email*</div>
  <div class="field" style="left:282px;top:158px;width:222px">Phone Number*</div>
  <div class="field" style="left:33px;top:218px;width:471px;height:84px">Message*</div>
  <div class="btn btn-brown" style="left:205px;top:330px;width:118px;height:46px;font-size:17px">SUBMIT</div>
</section>

<!-- footer -->
<footer class="abs footer">
  <h4 style="left:108px">About us</h4>
  <p class="blurb">Our qualified interior designer can also assist you with your colour selection as a part of our free colour consultancy service.If you are looking at painting your property, or have any questions, please don’t hesitate to call Ravi on 021 5550148.</p>
  <div class="sub"><span>Enter Email</span><b>SUBSCRIBE</b></div>

  <h4 style="left:506px">Quick Link</h4>
  <ul style="left:506px"><li>Home</li><li>About</li><li>Service</li><li>Latest News</li><li>Contact</li></ul>

  <h4 style="left:692px">Help Link</h4>
  <ul style="left:692px"><li>FAQ</li><li>Terms</li><li>Privacy</li><li>Support</li><li>Conditions</li></ul>

  <h4 style="left:870px">Address</h4>
  <div class="addr">
    <div><i></i>hello@kestrelpainters.co.nz</div>
    <div><i></i>021 555 0148</div>
    <div><i></i>Fernleigh, Northvale.</div>
  </div>

  <p class="copy">Copyright@2022.All Rights Reserved</p>
  <div class="badge" style="left:874px;width:50px;border-radius:8px;background:#3b6fc4" aria-label="Veltora paint partner badge"></div>
  <div class="badge" style="left:955px;width:125px;background:#1f5fb0" aria-label="Accredited painter badge"></div>
</footer>

</body>
</html>
```